Short-Term Rental Website - Management Services for Property Owner

We are looking for a website to advertise our short-term rental business, Bright Door Stay Management, currently www.brightdoor.ca. Hosted on WordPress.

We have the website main page language but we are looking for someone who is creative and can present the information in a trendy, cool and professional way. I like the closed design crowd job "Plumfield Marketing - SEM, Influencer website. FUN RETRO VIBES" (see attached pictures) in terms of how the page flows, icons and stock images, other connective imagery and design features

Our main competitor website is www.stayvora.com and we like how that website feels but we like the elegance of www.Halvorn-Trask.com (desktop) and main page of www.pombridge.ca (desktop version). We like the slow type video on pombridge.com.

MUST LOOK GOOD ON MOBILE. The mobile experience has to be good.

The content in terms of the language is in one of the attached files.

Our landing page requires the following sections;
- Revenue Maximization
- Services (I have included the content that we want highlighted but we are looking for someone to be creative with how these are displayed
- Pricing
- Featured Properties (display on a carousel) *must design a carousel that can be easily populated.
- Reviews (display on a carousel) *must design a carousel that can be easily populated.
- Contact Us (first name, last name, email, phone (required), description of property)

The header will have;
- Logo (link to main page)
- Pricing (link to pricing section found on the main page)
- Services (link to services section found on the main page)
- Properties (separate page)
- Contact (link to contact area on main page)

We would also need a coded template page that we could use to add additional pages as needed.

For the properties page, we need a landing page that would allow our guests to see all of our properties and a map view with the properties plotted on the map.

As we would collect personal information we would need a cookies/ privacy policy.

The colour palette should be on the light side. We do not want the website to have a dark feel. Colours should be consistent with that of our logo but we are open to creativity.

Target Market(s)

Investment property owners

Industry/Entity Type

Real Estate

Coding

Coded - Design and coding required

Number of Pages Required

2 page

Font styles to use
Sans Serif

Requirements
Must have
• Very strong and well designed landing page

Second page which showcases properttes

Template property page that can be easily reproduced

```html
<!DOCTYPE html>
<html lang="en">
<head>
<meta charset="utf-8">
<title>Bright Door Stay Management</title>
<link rel="stylesheet" href="https://fonts.googleapis.com/css2?family=Roboto:wght@400;500;700;900&family=Lato:wght@400;700&display=swap">
<style>
:root{
  --teal:#3d6b7b;
  --teal-dark:#2f5866;
  --ink:#222;
  --text:#444;
  --muted:#777;
  --dark:#2b2b2b;
  --light:#f4f4f4;
  --white:#fff;
  --star:#f0a01c;
}
*{box-sizing:border-box;margin:0;padding:0}
html,body{width:1200px;height:5245px;overflow:hidden}
body{position:relative;background:var(--white);font-family:"Lato",sans-serif;color:var(--text)}
.abs{position:absolute}
h1,h2,h3,h4,.head{font-family:"Roboto",sans-serif}

/* header */
.site-header{left:0;top:0;width:1200px;height:96px;background:var(--white)}
.brand{display:flex;align-items:center;gap:10px}
.brand-mark{width:30px;height:30px;background:var(--teal)}
.brand-name{font-family:"Roboto",sans-serif;font-weight:900;font-size:34px;color:var(--teal-dark);letter-spacing:-.5px}
.site-header .brand{position:absolute;left:143px;top:28px}
.main-nav{position:absolute;left:536px;top:41px;display:flex;gap:0}
.main-nav a{font-family:"Roboto",sans-serif;font-weight:500;font-size:15px;color:var(--ink);text-decoration:none;position:absolute;white-space:nowrap}
.main-nav a.active{color:var(--teal)}

/* hero */
.hero{left:0;top:96px;width:1200px;height:780px;overflow:hidden}
.hero-photo{position:absolute;inset:0;background:linear-gradient(160deg,#6b5c4d 0%,#8d7f6e 30%,#4b3d33 60%,#2e241e 100%)}
.hero-shade{position:absolute;inset:0;background:rgba(0,0,0,.18)}
.hero h1{position:absolute;left:290px;top:214px;width:620px;text-align:center;color:var(--white);font-weight:900;font-size:32px;line-height:40px;text-transform:uppercase}
.btn{display:flex;align-items:center;justify-content:center;font-family:"Roboto",sans-serif;font-weight:700;font-size:13px;text-transform:uppercase;text-decoration:none}
.btn-light{background:var(--white);color:var(--ink)}
.btn-teal{background:var(--teal);color:var(--white)}
.hero .btn{position:absolute;top:404px;width:157px;height:42px}
.dots{display:flex;gap:8px}
.dots span{width:12px;height:12px;border-radius:50%;border:2px solid var(--white)}
.dots span.on{background:var(--white)}
.hero .dots{position:absolute;left:562px;top:623px}
.hero-edge{position:absolute;left:0;bottom:0}

/* section titles */
.section-title{width:1200px;left:0;text-align:center;font-weight:900;font-size:37px;color:var(--ink);text-transform:uppercase}

/* services */
.service-card{width:292px;background:var(--white);box-shadow:0 2px 10px rgba(0,0,0,.14)}
.service-photo{position:relative;height:200px;overflow:hidden}
.service-photo .tone{position:absolute;inset:0}
.service-photo .veil{position:absolute;inset:0}
.service-icon{position:absolute;left:102px;top:32px;width:88px;height:88px;border:3px solid var(--white);border-radius:50%;display:flex;align-items:center;justify-content:center}
.service-card h3{position:absolute;left:0;top:138px;width:292px;text-align:center;color:var(--white);font-weight:700;font-size:16px;line-height:22px;text-transform:uppercase}
.service-card p{padding:18px 26px 0;text-align:center;font-size:13px;line-height:21px;color:var(--text);height:120px;overflow:hidden}
.service-card .more{display:block;text-align:center;margin-top:8px}

/* pricing */
.pricing{left:0;top:1921px;width:1200px;height:568px;background:linear-gradient(180deg,#4c7787 0%,#3b6676 100%)}
.pricing h2{position:absolute;left:0;top:60px;width:1200px;text-align:center;font-weight:500;font-size:38px;color:var(--white)}
.pricing .rule{position:absolute;left:566px;top:112px;width:68px;height:3px;background:var(--white)}
.share{position:absolute;left:145px;top:192px;width:380px;color:var(--white)}
.share h3{font-weight:700;font-size:28px;line-height:36px;text-transform:uppercase}
.share .pct{font-family:"Roboto",sans-serif;font-weight:700;font-size:54px;margin:16px 0 10px}
.share p{font-size:18px;line-height:26px;margin-bottom:18px}
.pricing-notes{position:absolute;left:623px;top:190px;width:450px;color:var(--white);font-size:18px;line-height:24px}
.pricing-notes p{margin-bottom:18px}
.btn-dark{background:#1f1f1f;color:var(--white)}
.pricing .btn-dark{position:absolute;left:623px;top:422px;width:324px;height:42px}

/* properties */
.property-grid{left:0;top:2644px;width:1200px;height:729px}
.tile{position:absolute;overflow:hidden}
.tile-feature{display:flex;flex-direction:column;align-items:center;justify-content:center;background:rgba(61,107,123,.82);color:var(--white)}
.tile-feature h4{font-weight:700;font-size:22px;line-height:31px;text-align:center;text-transform:uppercase}
.prop-dots{left:560px;top:3409px;display:flex;gap:11px}
.prop-dots span{width:6px;height:6px;border-radius:50%;background:#555}

/* reviews */
.review-card{width:291px;height:322px;background:var(--white);box-shadow:0 2px 10px rgba(0,0,0,.14);text-align:center;padding-top:62px}
.avatar{position:absolute;left:103px;top:-44px;width:86px;height:86px;border-radius:50%;border:3px solid var(--white);box-shadow:0 2px 6px rgba(0,0,0,.2)}
.review-card h4{font-weight:700;font-size:14px;color:var(--ink)}
.review-card .role{font-size:12px;color:var(--text);margin-top:4px}
.review-card p{font-size:13px;line-height:21px;color:var(--text);padding:14px 26px 0}
.stars{color:var(--star);font-size:15px;letter-spacing:2px;margin-top:10px}
.quote{font-family:"Roboto",sans-serif;font-weight:900;font-size:46px;line-height:40px;color:var(--ink);margin-top:6px}

/* contact */
.work{left:0;top:4060px;width:1200px;height:658px}
.work h2{position:absolute;left:0;top:148px;width:1200px;text-align:center;font-weight:500;font-size:36px;color:var(--white);text-transform:uppercase}
.work .lead{position:absolute;left:0;top:206px;width:1200px;text-align:center;font-size:15px;color:var(--white)}
.field{position:absolute;background:var(--white);font-size:13px;color:#555;padding:0 24px;display:flex;align-items:center}
.field.tall{align-items:flex-start;padding-top:22px}
.work .btn{position:absolute;left:505px;top:527px;width:188px;height:41px;border-radius:21px;font-size:14px}

/* footer */
.footer{left:0;top:4718px;width:1200px;height:350px;background:var(--light)}
.footer h4{position:absolute;top:72px;font-weight:500;font-size:17px;color:var(--ink);text-transform:uppercase}
.footer .row{position:absolute;display:flex;gap:12px;font-size:13px;line-height:18px;color:#333}
.mini-input{position:absolute;left:446px;width:271px;height:37px;background:var(--white);border:1px solid #d8d8d8;font-size:11px;color:#555;padding-left:12px;display:flex;align-items:center}
.footer .btn-teal{position:absolute;left:446px;top:220px;width:114px;height:34px;font-size:12px}
.links{position:absolute;left:780px;top:112px;font-size:13px;line-height:26.5px;color:#333;list-style:none}
.social{position:absolute;left:949px;top:108px;list-style:none}
.social li{display:flex;align-items:center;gap:10px;height:40px;font-size:13px;color:#333}
.social .ring{width:28px;height:28px;border:1.5px solid #444;border-radius:50%}
.bottom{left:0;top:5068px;width:1200px;height:177px;background:var(--white)}
.bottom .brand{position:absolute;left:468px;top:42px}
.bottom p{position:absolute;left:0;top:112px;width:1200px;text-align:center;font-size:13px;color:#333}
</style>
</head>
<body>

<header class="site-header abs">
  <a class="brand" href="#"><span class="brand-mark"></span><span class="brand-name">Bright Door</span></a>
  <nav class="main-nav">
    <a class="active" href="#" style="left:0">HOME</a>
    <a href="#pricing" style="left:79px">PRICING</a>
    <a href="#services" style="left:181px">SERVICES</a>
    <a href="#" style="left:289px">PROPERTIES</a>
    <a href="#contact" style="left:421px">CONTACT US</a>
  </nav>
</header>

<section class="hero abs">
  <div class="hero-photo" role="img" aria-label="Bright modern living room with a leather sofa, large windows and two agents showing the home"></div>
  <div class="hero-shade"></div>
  <h1>Your property's value will be optimized to reach its potential through our revenue maximization services.</h1>
  <a class="btn btn-light" href="#" style="left:436px">Learn More</a>
  <a class="btn btn-teal" href="#" style="left:605px">Free Quote</a>
  <div class="dots"><span class="on"></span><span></span><span></span><span></span></div>
  <svg class="hero-edge" width="1200" height="80" viewBox="0 0 1200 80">
    <polygon points="0,80 0,60 600,8 1200,60 1200,80" fill="#3d6b7b"/>
    <polygon points="0,80 0,74 600,22 1200,74 1200,80" fill="#fff"/>
  </svg>
</section>

<h2 id="services" class="section-title abs" style="top:884px">Our Services</h2>

<!-- service cards -->
<article class="service-card abs" style="left:136px;top:980px;height:398px">
  <div class="service-photo">
    <div class="tone" role="img" aria-label="Person searching listings on a laptop" style="background:linear-gradient(135deg,#8b7a68,#4a4038)"></div>
    <svg class="veil" width="292" height="200"><polygon points="0,0 292,0 292,200 146,196 0,200" fill="rgba(30,30,30,.45)"/><polygon points="0,200 292,200 292,190 146,175 0,190" fill="#fff"/></svg>
    <div class="service-icon"><svg width="46" height="46" viewBox="0 0 46 46" fill="none" stroke="#fff" stroke-width="2"><circle cx="23" cy="23" r="18"/><ellipse cx="23" cy="23" rx="8" ry="18"/><line x1="5" y1="23" x2="41" y2="23"/></svg></div>
    <h3>Staylist Search Engine<br>Optimization</h3>
  </div>
  <p>Staylist ranks all listings using an algorithm (much like Searchly) and our optimization techniques allow your listing to appear higher in search results and receive more bookings.</p>
  <a class="more" href="#"><svg width="26" height="14" viewBox="0 0 26 14" fill="none" stroke="#3d6b7b" stroke-width="2"><path d="M1 7h23M18 1l6 6-6 6"/></svg></a>
</article>

<article class="service-card abs" style="left:453px;top:988px;height:398px">
  <div class="service-photo">
    <div class="tone" role="img" aria-label="Suburban house front under a blue sky" style="background:linear-gradient(180deg,#7b92a8,#3c4a52)"></div>
    <svg class="veil" width="292" height="200"><polygon points="0,0 292,0 292,200 0,200" fill="rgba(30,30,30,.4)"/><polygon points="0,200 292,200 292,190 146,175 0,190" fill="#fff"/></svg>
    <div class="service-icon"><svg width="46" height="46" viewBox="0 0 46 46" fill="none" stroke="#fff" stroke-width="2"><path d="M24 6h14v14L20 38 6 24z"/><circle cx="32" cy="12" r="2"/><path d="M18 22h6M17 28h8"/></svg></div>
    <h3>Proprietary Pricing<br>Tool</h3>
  </div>
  <p>We have developed a proprietary pricing tool that allows us to determine future nightly rates based on demand. This tool has led us to managing the #1 &amp; #5 Highest Revenue 2-Bedroom</p>
  <a class="more" href="#"><svg width="26" height="14" viewBox="0 0 26 14" fill="none" stroke="#3d6b7b" stroke-width="2"><path d="M1 7h23M18 1l6 6-6 6"/></svg></a>
</article>

<article class="service-card abs" style="left:770px;top:980px;height:398px">
  <div class="service-photo">
    <div class="tone" role="img" aria-label="Manager on a headset at a desk" style="background:linear-gradient(135deg,#9aa2a8,#4a4f55)"></div>
    <svg class="veil" width="292" height="200"><polygon points="0,0 292,0 292,200 0,200" fill="rgba(30,30,30,.42)"/><polygon points="0,200 292,200 292,190 146,175 0,190" fill="#fff"/></svg>
    <div class="service-icon"><svg width="46" height="46" viewBox="0 0 46 46" fill="none" stroke="#fff" stroke-width="2"><rect x="8" y="10" width="28" height="26"/><path d="M8 17h28M15 6v8M29 6v8M14 23h4M21 23h4M28 23h4M14 29h4M21 29h4"/><circle cx="34" cy="34" r="6" fill="#555"/><path d="M31 34l2 2 4-4"/></svg></div>
    <h3>Strategic Calendar<br>Management</h3>
  </div>
  <p>Our strategy focuses on future bookings being as long as possible. This, along with other techniques, has resulted in our properties averaging an ~85% occupancy rate which is</p>
  <a class="more" href="#"><svg width="26" height="14" viewBox="0 0 26 14" fill="none" stroke="#3d6b7b" stroke-width="2"><path d="M1 7h23M18 1l6 6-6 6"/></svg></a>
</article>

<article class="service-card abs" style="left:136px;top:1403px;height:402px">
  <div class="service-photo">
    <div class="tone" role="img" aria-label="Clean bright kitchen interior" style="background:linear-gradient(135deg,#c6c2bc,#6a655f)"></div>
    <svg class="veil" width="292" height="200"><polygon points="0,0 292,0 292,200 0,200" fill="rgba(30,30,30,.45)"/><polygon points="0,200 292,200 292,190 146,175 0,190" fill="#fff"/></svg>
    <div class="service-icon"><svg width="46" height="46" viewBox="0 0 46 46" fill="none" stroke="#fff" stroke-width="2"><path d="M6 22L23 8l17 14"/><rect x="11" y="20" width="24" height="18"/><rect x="18" y="26" width="10" height="12"/></svg></div>
    <h3>Home Care</h3>
  </div>
  <p>Professional cleaning with unique cleaning guide Staging guide created for consistent appearance Inventory and replenishment of essentials Property inspection between</p>
  <a class="more" href="#"><svg width="26" height="14" viewBox="0 0 26 14" fill="none" stroke="#3d6b7b" stroke-width="2"><path d="M1 7h23M18 1l6 6-6 6"/></svg></a>
</article>

<article class="service-card abs" style="left:453px;top:1411px;height:402px">
  <div class="service-photo">
    <div class="tone" role="img" aria-label="Hand pressing a smart door lock keypad" style="background:linear-gradient(135deg,#2e4a66,#101d2c)"></div>
    <svg class="veil" width="292" height="200"><polygon points="0,0 292,0 292,200 0,200" fill="rgba(20,20,30,.3)"/><polygon points="0,200 292,200 292,190 146,175 0,190" fill="#fff"/></svg>
    <div class="service-icon"><svg width="46" height="46" viewBox="0 0 46 46" fill="none" stroke="#fff" stroke-width="2"><rect x="13" y="6" width="20" height="34" rx="3"/><rect x="17" y="20" width="12" height="10"/><path d="M19 20v-4a4 4 0 0 1 8 0v4"/></svg></div>
    <h3>Safety &amp; Security</h3>
  </div>
  <p>Smart Lock (Condo Compliant) Sensory Security Devices (non-invasive, real-time data) Insurance for damage provided by Staylist* Enhanced Guest Screening Ongoing Guest Risk</p>
  <a class="more" href="#"><svg width="26" height="14" viewBox="0 0 26 14" fill="none" stroke="#3d6b7b" stroke-width="2"><path d="M1 7h23M18 1l6 6-6 6"/></svg></a>
</article>

<article class="service-card abs" style="left:770px;top:1403px;height:402px">
  <div class="service-photo">
    <div class="tone" role="img" aria-label="Colleagues reviewing results at a laptop" style="background:linear-gradient(135deg,#8f8a80,#433e38)"></div>
    <svg class="veil" width="292" height="200"><polygon points="0,0 292,0 292,200 0,200" fill="rgba(30,30,30,.45)"/><polygon points="0,200 292,200 292,190 146,175 0,190" fill="#fff"/></svg>
    <div class="service-icon"><svg width="46" height="46" viewBox="0 0 46 46" fill="none" stroke="#fff" stroke-width="2"><rect x="8" y="10" width="30" height="22"/><path d="M14 28v-6M20 28v-10M26 28v-4M32 28v-12M18 38h10M23 32v6"/></svg></div>
    <h3>Performance<br>Optimization</h3>
  </div>
  <p>Proprietary Pricing Tool used Only by Bright Door Strategic Calendar Management #1 &amp; #5 Highest Revenue 2-Bedroom Listings in Calgary Enhanced Analytics (above what</p>
  <a class="more" href="#"><svg width="26" height="14" viewBox="0 0 26 14" fill="none" stroke="#3d6b7b" stroke-width="2"><path d="M1 7h23M18 1l6 6-6 6"/></svg></a>
</article>

<section id="pricing" class="pricing abs" role="img" aria-label="Street of homes under a teal tint">
  <h2>Our Pricing</h2>
  <div class="rule"></div>
  <div class="share">
    <h3>Bright Door's share<br>of the nightly revenue</h3>
    <div class="pct">20%</div>
    <p>All money goes to your bank account, we invoice you one-time per month.</p>
    <p>There are no additional fees and best of all, no surprises!</p>
  </div>
  <div class="pricing-notes">
    <p>Our pricing structure is simple and easy to understand, that is by design!</p>
    <p>The nightly revenue is split between the Owner and Bright Door, 80% &amp; 20% respectively.</p>
    <p>The cleaning fee is paid for by the guest which covers all cleaning between guests. We do not take a fee from cleaning.</p>
  </div>
  <a class="btn btn-dark" href="#">Click here to see an example</a>
</section>

<h2 class="section-title abs" style="top:2550px">Featured Properties</h2>

<section class="property-grid abs">
  <div class="tile" role="img" aria-label="Modern brick apartment building" style="left:0;top:0;width:400px;height:326px;background:linear-gradient(160deg,#a9c1d8,#8a6a52 60%,#5d4a3a)"></div>
  <div class="tile" role="img" aria-label="Open-plan kitchen interior" style="left:400px;top:0;width:400px;height:326px;background:linear-gradient(160deg,#c9cfd2,#8d9598)">
    <div class="tile tile-feature" style="inset:0">
      <h4>Nemo enim ipsam<br>voluptatem</h4>
      <svg width="38" height="30" viewBox="0 0 38 30" fill="none" stroke="#fff" stroke-width="4"><path d="M2 15h32M22 3l12 12-12 12"/></svg>
    </div>
  </div>
  <div class="tile" role="img" aria-label="Blue two-storey house lit at dusk" style="left:800px;top:0;width:400px;height:326px;background:linear-gradient(160deg,#7a8eb0,#3d4763 60%,#5a5a3e)"></div>
  <div class="tile" role="img" aria-label="Living room with white sofa and staircase" style="left:0;top:326px;width:400px;height:403px;background:linear-gradient(160deg,#e8e4de,#b9ab98 60%,#6b5a4a)"></div>
  <div class="tile" role="img" aria-label="Large family house with green lawn and driveway" style="left:400px;top:326px;width:800px;height:403px;background:linear-gradient(180deg,#9fc3e0 0%,#c8d2c0 40%,#8a8470 60%,#5a8a3c 100%)"></div>
</section>
<div class="prop-dots abs"><span></span><span></span><span></span><span></span><span></span></div>

<h2 class="section-title abs" style="top:3510px">Our Reviews</h2>

<svg class="abs" style="left:84px;top:3778px" width="18" height="30" viewBox="0 0 18 30" fill="none" stroke="#777" stroke-width="3"><path d="M15 2L3 15l12 13"/></svg>
<svg class="abs" style="left:1098px;top:3778px" width="18" height="30" viewBox="0 0 18 30" fill="none" stroke="#777" stroke-width="3"><path d="M3 2l12 13L3 28"/></svg>

<article class="review-card abs" style="left:143px;top:3646px">
  <div class="avatar" role="img" aria-label="Reviewer portrait" style="background:linear-gradient(#8a8a8a,#333)"></div>
  <h4>Liam Porter</h4>
  <div class="role">Bright Door Stay Management</div>
  <p>Sed ut perspiciatis unde omnis iste natus sit voluptatem accusantium doloremque laudantium, totam rem aperiam, eaque ipsa quae ab illo inventore veritatis et quasi architecto beatae vitae dicta sunt explicabo.</p>
  <div class="stars">★★★★★</div>
  <div class="quote">“</div>
</article>
<article class="review-card abs" style="left:452px;top:3677px">
  <div class="avatar" role="img" aria-label="Reviewer portrait" style="background:linear-gradient(#b8c2cc,#4a5560)"></div>
  <h4>Nadia Chen</h4>
  <div class="role">Bright Door Stay Management</div>
  <p>Sed ut perspiciatis unde omnis iste natus sit voluptatem accusantium doloremque laudantium, totam rem aperiam, eaque ipsa quae ab illo inventore veritatis et quasi architecto beatae vitae dicta sunt explicabo.</p>
  <div class="stars">★★★★★</div>
  <div class="quote">“</div>
</article>
<article class="review-card abs" style="left:764px;top:3646px">
  <div class="avatar" role="img" aria-label="Reviewer portrait" style="background:linear-gradient(#9a9a9a,#3a3a3a)"></div>
  <h4>Owen Reyes</h4>
  <div class="role">Bright Door Stay Management</div>
  <p>Sed ut perspiciatis unde omnis iste natus sit voluptatem accusantium doloremque laudantium, totam rem aperiam, eaque ipsa quae ab illo inventore veritatis et quasi architecto beatae vitae dicta sunt explicabo.</p>
  <div class="stars">★★★★★</div>
  <div class="quote">“</div>
</article>

<section id="contact" class="work abs">
  <svg class="abs" style="left:0;top:0" width="1200" height="658" viewBox="0 0 1200 658">
    <polygon points="0,70 600,30 1200,0 1200,658 0,658" fill="#3d6b7b"/>
    <polygon points="0,84 600,44 1200,16 1200,658 0,658" fill="#2b2b2b"/>
  </svg>
  <h2>Work With Us</h2>
  <p class="lead">Interested in working with us? Fill out the form below or give us a call!</p>
  <div class="field" style="left:198px;top:269px;width:370px;height:61px">First Name</div>
  <div class="field" style="left:599px;top:269px;width:401px;height:61px">Last Name</div>
  <div class="field" style="left:198px;top:350px;width:370px;height:61px">Email address</div>
  <div class="field tall" style="left:599px;top:348px;width:401px;height:139px">Description of property</div>
  <div class="field" style="left:198px;top:430px;width:370px;height:59px">Phone</div>
  <a class="btn btn-teal" href="#">Submit</a>
</section>

<footer class="footer abs">
  <h4 style="left:143px">Contact Us</h4>
  <div class="row" style="left:148px;top:116px"><svg width="14" height="18" viewBox="0 0 14 18"><path d="M7 0a7 7 0 0 0-7 7c0 5 7 11 7 11s7-6 7-11a7 7 0 0 0-7-7z" fill="#3d6b7b"/><circle cx="7" cy="7" r="2.5" fill="#f4f4f4"/></svg><span>939 enim ipsam voluptatem<br>quia voluptas sit</span></div>
  <div class="row" style="left:148px;top:168px"><svg width="14" height="16" viewBox="0 0 14 16"><path d="M3 1l3 3-2 2c1 2 3 4 5 5l2-2 3 3-2 3C6 15 0 9 1 3z" fill="#3d6b7b"/></svg><span>Phone:<br>403-555-0187</span></div>
  <div class="row" style="left:148px;top:218px"><svg width="16" height="12" viewBox="0 0 16 12"><rect width="16" height="12" fill="#3d6b7b"/><path d="M0 0l8 6 8-6" stroke="#f4f4f4" fill="none"/></svg><span>Email:<br>info@brightdoor.ca</span></div>

  <h4 style="left:446px">Sign up for newsletter</h4>
  <div class="mini-input" style="top:116px">First Name</div>
  <div class="mini-input" style="top:166px">Email</div>
  <a class="btn btn-teal" href="#">Submit</a>

  <h4 style="left:776px">Quick Links</h4>
  <ul class="links"><li>Home</li><li>Pricing</li><li>Services</li><li>Properties</li><li>Contact us</li></ul>

  <h4 style="left:949px">Social</h4>
  <ul class="social">
    <li><span class="ring"></span>Friendline</li>
    <li><span class="ring"></span>Chirpnet</li>
    <li><span class="ring"></span>Circleplus</li>
    <li><span class="ring"></span>Viewcast</li>
  </ul>
</footer>

<section class="bottom abs">
  <a class="brand" href="#"><span class="brand-mark"></span><span class="brand-name">Bright Door</span></a>
  <p>Bright Door Stay Management © 2020 All Rights Reserved | Privacy Policy | Terms and Conditions</p>
</section>

</body>
</html>
```